Product label for herbal salves, lotions, soaps and tinctures

We need a very simple, clean and organic looking label that can be used for an ointment jar, a lotion bottle and a dropper bottle.
We have an existing logo (see attached). We like the colors white, olive green, gold and black. It needs to include product name as dominant and logo. It also needs to include an ingredient list, and usage statement. Include weight of product, distributed by, made in the USA, and NQB statement.
Example of what needs to be present:
Logo
Name: Calmwick Balm
Used for: For Muscle Aches, Arthritis, Tendonitis, Headaches
To Use: For muscle aches, arthritis and tendonitis, massage into affected area. For tension headache apply to neck, temples and forehead.
Store in a cool and dry place, away from direct heat and sunlight.
Weight of product: 1.75
DIST. BY: Brookmere Herbal
Made in the USA
This product is not intended to diagnose, treat, cure
or prevent any disease. Not regulated
by the NQB. Please consult your health care practitioner
before using product. Discontinue use if any adverse reaction occurs.
Ingredient list:
Wildcrafted Ingredients:
Ashwagandha Root, Peppermint Leaf, Hops Flowers, St. John’s Wort Herb, Arnica Flowers, Green Tea Leaf, Alfalfa Leaf, Dandelion Root, Burdock Root, Chickweed Herb, Chaparral Leaf, Yarrow Flowers, Boneset Herb, Moringa Leaf, Meadowsweet Herb, Nettle Leaf
Organic Ingredients:
Olive Oil, Aloe Leaf, Sweet Birch Bark, Helichrysum Flowers, Holy Basil Leaf, Borage Herb, Ginger Root, Angelica Root, White Willow Bark, Mustard Seed, Beeswax, Vitamin E, Essential Oils
Dimensions of Jar:
Circumference: 7 in.
Height: 1 in.

```html
<!DOCTYPE html>
<html lang="en">
<head>
<meta charset="utf-8">
<title>Brookmere Herbal – Calmwick Balm Label</title>
<link href="https://fonts.googleapis.com/css2?family=Montserrat:wght@400;500;600;700&display=swap" rel="stylesheet">
<style>
  :root {
    --stage: #e9e6df;
    --label-black: #121110;
    --label-black-2: #1c1a17;
    --olive: #7d8f3a;
    --olive-band: #6b7a32;
    --gold: #c9a94f;
    --gold-muted: #b5a27a;
    --white: #f4f2ec;
    --amber: #d99a2b;
    --rule: rgba(201, 169, 79, 0.35);
  }
  * { box-sizing: border-box; margin: 0; padding: 0; }
  html, body {
    width: 1200px; height: 900px; overflow: hidden;
    background: var(--stage);
    font-family: "Montserrat", sans-serif;
  }
  .canvas {
    width: 1200px; height: 900px;
    display: flex; align-items: center; justify-content: center;
  }
  .wrap-label {
    width: 1100px; height: 520px;
    display: flex;
    background: linear-gradient(180deg, var(--label-black-2), var(--label-black));
    border-radius: 6px;
    box-shadow: 0 10px 30px rgba(0,0,0,0.18);
    color: var(--white);
  }
  .front-panel {
    width: 520px; height: 100%;
    display: flex; flex-direction: column; align-items: center;
    padding: 56px 40px 36px;
    border-right: 1px dashed var(--rule);
  }
  .brand {
    display: flex; align-items: center; gap: 12px;
  }
  .brand-dot {
    width: 18px; height: 18px; border-radius: 50%;
    background: var(--olive);
  }
  .brand-name {
    font-weight: 700; font-size: 34px; color: var(--olive);
    letter-spacing: 0.5px;
  }
  .product-name { margin-top: 70px; text-align: center; color: var(--gold-muted); }
  .product-name .line-1 {
    display: block; font-weight: 500; font-size: 40px; letter-spacing: 3px;
  }
  .product-name .line-2 {
    display: block; font-weight: 600; font-size: 84px; letter-spacing: 6px; line-height: 1.05;
  }
  .uses-band {
    margin-top: 24px;
    background: var(--olive-band);
    color: var(--white);
    font-weight: 600; font-size: 17px;
    padding: 7px 18px; border-radius: 4px;
    white-space: nowrap;
  }
  .net-weight {
    margin-top: auto;
    font-size: 15px; font-weight: 500; color: var(--white);
  }
  .back-panel {
    flex: 1; display: flex; gap: 30px;
    padding: 44px 40px 36px;
  }
  .back-brand { margin-bottom: 20px; }
  .back-brand .brand-name { font-size: 22px; }
  .back-brand .brand-dot { width: 12px; height: 12px; }
  .ingredients { width: 300px; }
  .section-title {
    font-weight: 700; font-size: 16px; color: var(--white); margin: 10px 0 8px;
  }
  .ingredient-list { font-size: 11.5px; line-height: 1.6; color: #d9d6cc; }
  .usage { flex: 1; font-size: 11.5px; line-height: 1.6; color: #d9d6cc; padding-top: 48px; }
  .usage p { margin-bottom: 12px; }
  .usage strong { color: var(--white); font-weight: 700; font-size: 14px; }
  .distribution { margin-top: 6px; }
  .notice {
    margin-top: 8px;
    background: var(--amber); color: var(--label-black);
    padding: 8px 10px; border-radius: 3px; font-size: 10.5px; line-height: 1.5; font-weight: 500;
  }
</style>
</head>
<body>
<main class="canvas">
  <article class="wrap-label">
    <section class="front-panel">
      <div class="brand">
        <span class="brand-dot"></span>
        <span class="brand-name">Brookmere Herbal</span>
      </div>
      <h1 class="product-name">
        <span class="line-1">CALMWICK</span>
        <span class="line-2">BALM</span>
      </h1>
      <p class="uses-band">For Muscle Aches, Arthritis, Tendonitis, Headaches</p>
      <p class="net-weight">Net Weight : 1.75gm.</p>
    </section>

    <section class="back-panel">
      <div class="ingredients">
        <div class="brand back-brand">
          <span class="brand-dot"></span>
          <span class="brand-name">Brookmere Herbal</span>
        </div>
        <h2 class="section-title">Wildcrafted Ingredients:</h2>
        <p class="ingredient-list">Ashwagandha Root, Peppermint Leaf, Hops Flowers, St. John’s Wort Herb, Arnica Flowers, Green Tea Leaf, Alfalfa Leaf, Dandelion Root, Burdock Root, Chickweed Herb, Chaparral Leaf, Yarrow Flowers, Boneset Herb, Moringa Leaf, Meadowsweet Herb, Nettle Leaf</p>
        <h2 class="section-title">Organic Ingredients:</h2>
        <p class="ingredient-list">Olive Oil, Aloe Leaf, Sweet Birch Bark, Helichrysum Flowers, Holy Basil Leaf, Borage Herb, Ginger Root, Angelica Root, White Willow Bark, Mustard Seed, Beeswax, Vitamin E, Essential Oils</p>
      </div>
      <div class="usage">
        <p><strong>To Use:</strong><br>For muscle aches, arthritis and tendonitis, massage into affected area. For tension headache apply to neck, temples and forehead.</p>
        <p>Store in a cool and dry place, away from direct heat and sunlight.</p>
        <p class="distribution">Dist. by: Brookmere Herbal<br>Made in the USA</p>
        <p class="notice">This product is not intended to diagnose, treat, cure or prevent any disease. Not regulated by the NQB. Please consult your health care practitioner before using product. Discontinue use if any adverse reaction occurs.</p>
      </div>
    </section>
  </article>
</main>
</body>
</html>
```